I need a flyer made , the flyer can be one page or two pages or three pages . I will be posting this on Instagram and social media platforms. I am a luxury home builder , I am looking to hire a construction project manager . Below are some examples and ideas what can be on the flyer

We’re looking for a construction project manager who’s passionate about building luxury homes at the highest standards
We’re hiring construction project manager
* Experience 5+ years in residential project management with a strong portfolio of completed homes.
* location : Bergen County NJ
* excellent leadership skills, leads teams with confidence and clarity
* communicates seamlessly with architects , engineers, designers and clients
*knows how to manage budgets and timelines without compromising quality
*solves problems with a positive solution first mindset
* pays attention to every detail because in luxury the small things are the big things

Apply now , link in bio or DM to connect.

My logo is attached, my web site www.ridgelanebuilders.com
My style is modern but still warm and inviting. I like a clean classy look .
Updates

Please don’t add any images of chairs or people to the flyer , I do not want people on my flyer. Do not add standard images of offices and houses , we are luxury builders , we build homes over 2 million dollars. Keep a classy , simple modern look . High end .

You can add a white hard hat with my logo on it for a image , this is a suggestion does not have to be on my flyer ,

```html
<!DOCTYPE html>
<html lang="en">
<head>
<meta charset="utf-8">
<title>Ridgelane Builders – Hiring Carousel</title>
<link href="https://fonts.googleapis.com/css2?family=Montserrat:wght@300;400;500;600;700;800&display=swap" rel="stylesheet">
<style>
  :root {
    --stage: #b9b9b9;
    --label-ink: #3b3b3b;
    --slide-bg: #1e1e1e;
    --card: #625e58;
    --card-arc: #6c6861;
    --cta-box: #3e3e40;
    --band: #625d56;
    --white: #ffffff;
    --gold-light: #f4d6b3;
    --gold-mid: #e3b58e;
    --gold-dark: #b98160;
  }
  * { margin: 0; padding: 0; box-sizing: border-box; }
  html, body { width: 1200px; height: 865px; overflow: hidden; }
  body {
    background: var(--stage);
    font-family: "Montserrat", sans-serif;
    position: relative;
  }
  .slide-label {
    position: absolute;
    top: 67px;
    width: 208px;
    height: 42px;
    border: 1px solid var(--label-ink);
    border-radius: 21px;
    display: flex; align-items: center; justify-content: center;
    font-weight: 700;
    font-size: 26px;
    letter-spacing: -0.5px;
    color: var(--label-ink);
  }
  .slide-label--one { left: 228px; }
  .slide-label--two { left: 785px; }

  .slide {
    position: absolute;
    top: 169px;
    width: 544px;
    height: 544px;
    background: var(--slide-bg);
    overflow: hidden;
    color: var(--white);
  }
  .slide--intro { left: 44px; }
  .slide--requirements { left: 607px; }

  .slide__pattern {
    position: absolute; inset: 0;
    background: radial-gradient(ellipse at 85% 20%, #2a2724 0%, var(--slide-bg) 60%);
  }
  .slide__shapes { position: absolute; inset: 0; width: 544px; height: 544px; }

  .brand {
    position: absolute;
    font-weight: 400;
    font-size: 17px;
    letter-spacing: 1.5px;
    color: var(--white);
    display: flex; align-items: center; gap: 8px;
  }
  .brand__mark {
    width: 9px; height: 9px; background: var(--white);
  }
  .slide--intro .brand { left: 88px; top: 36px; }
  .slide--requirements .brand { left: 58px; top: 31px; }

  .intro__lead {
    position: absolute; left: 109px; top: 130px;
    font-size: 13.6px; line-height: 17.6px; font-weight: 400;
    letter-spacing: 0.2px;
  }
  .intro__were {
    position: absolute; left: 104px; top: 198px;
    font-size: 46px; font-weight: 300; letter-spacing: 0.5px;
  }
  .gold-text {
    background: linear-gradient(90deg, var(--gold-light) 0%, var(--gold-mid) 55%, var(--gold-dark) 100%);
    -webkit-background-clip: text; background-clip: text;
    color: transparent;
  }
  .intro__hiring {
    position: absolute; left: 100px; top: 224px;
    font-size: 76px; font-weight: 800; letter-spacing: -2px;
  }
  .role-pill {
    position: absolute; left: 91px; top: 343px;
    width: 248px; height: 35px;
    border: 1px solid var(--white);
    border-radius: 18px;
    display: flex; align-items: center; justify-content: center;
    font-size: 14.2px; font-weight: 400;
  }
  .role-pill strong { font-weight: 700; margin-right: 4px; }
  .role-sub {
    position: absolute; left: 105px; top: 383px;
    font-size: 14.5px; font-weight: 400;
  }
  .cta__title {
    position: absolute; left: 396px; top: 336px;
    font-size: 26px; line-height: 27px; font-weight: 700; letter-spacing: -0.3px;
  }
  .cta__note {
    position: absolute; left: 396px; top: 405px;
    font-size: 11.8px; line-height: 14.4px; font-weight: 400;
  }
  .site-url {
    position: absolute; right: 42px; top: 503px;
    font-size: 12.6px; font-weight: 600; letter-spacing: 0.2px;
  }

  .req__title {
    position: absolute; left: 80px; top: 120px;
    font-size: 26px; font-weight: 700; letter-spacing: 0.3px;
  }
  .req__rule {
    position: absolute; left: 79px; top: 160px;
    width: 60px; height: 1.5px; background: var(--white);
  }
  .req__list { list-style: none; }
  .req__item {
    position: absolute; left: 82px;
    display: flex; gap: 9px;
    font-size: 11.6px; line-height: 15px; font-weight: 400;
  }
  .req__item svg { flex: none; width: 11px; height: 11px; margin-top: 2px; }
  .req__item--wide { line-height: 19.5px; }
  .req__item--wide svg { margin-top: 4px; }
</style>
</head>
<body>

<div class="slide-label slide-label--one">SLIDE 1</div>
<div class="slide-label slide-label--two">SLIDE 2</div>

<!-- Slide 1: announcement -->
<section class="slide slide--intro">
  <div class="slide__pattern" role="img" aria-label="Fine topographic contour line pattern in dark bronze"></div>
  <svg class="slide__shapes" viewBox="0 0 1028 1028" aria-hidden="true">
    <defs>
      <clipPath id="intro-card-clip">
        <path d="M214 182 H814 Q884 182 884 252 V820 L214 852 Q144 855 144 785 V252 Q144 182 214 182 Z"/>
      </clipPath>
    </defs>
    <path fill="var(--card)" d="M214 182 H814 Q884 182 884 252 V820 L214 852 Q144 855 144 785 V252 Q144 182 214 182 Z"/>
    <circle clip-path="url(#intro-card-clip)" cx="884" cy="200" r="237" fill="none" stroke="var(--card-arc)" stroke-width="55"/>
    <path fill="var(--cta-box)" d="M764 594 H951 V912 L694 930 V664 Q694 594 764 594 Z"/>
    <path fill="var(--band)" d="M0 1028 Q40 962 120 955 L1028 880 V1028 Z"/>
  </svg>

  <div class="brand"><span class="brand__mark"></span>Ridgelane Builders</div>

  <p class="intro__lead">Looking For A Construction Project Manager<br>Who’s Passionate About Building Luxury<br>Homes At The Highest Standards</p>
  <p class="intro__were">We’re</p>
  <p class="intro__hiring gold-text">Hiring</p>

  <div class="role-pill"><strong>Construction</strong> Project Manager</div>
  <p class="role-sub">for Luxury Homes</p>

  <p class="cta__title">Apply<br>Now!</p>
  <p class="cta__note">link in bio or<br>DM to connect</p>

  <p class="site-url">www.ridgelanebuilders.com</p>
</section>

<!-- Slide 2: requirements -->
<section class="slide slide--requirements">
  <div class="slide__pattern" role="img" aria-label="Fine topographic contour line pattern in dark bronze"></div>
  <svg class="slide__shapes" viewBox="0 0 1028 1028" aria-hidden="true">
    <defs>
      <clipPath id="req-card-clip">
        <path d="M175 147 H851 Q921 147 921 217 V755 Q921 822 851 826 L185 888 Q105 892 105 815 V217 Q105 147 175 147 Z"/>
      </clipPath>
    </defs>
    <path fill="var(--card)" d="M175 147 H851 Q921 147 921 217 V755 Q921 822 851 826 L185 888 Q105 892 105 815 V217 Q105 147 175 147 Z"/>
    <circle clip-path="url(#req-card-clip)" cx="921" cy="150" r="237" fill="none" stroke="var(--card-arc)" stroke-width="55"/>
    <path fill="var(--band)" d="M0 1028 Q40 962 120 955 L1028 880 V1028 Z"/>
  </svg>

  <div class="brand"><span class="brand__mark"></span>Ridgelane Builders</div>

  <h2 class="req__title gold-text">Requirements :</h2>
  <div class="req__rule"></div>

  <ul class="req__list">
    <li class="req__item" style="top:193px"><svg viewBox="0 0 12 12"><rect x="0.6" y="0.6" width="10.8" height="10.8" rx="3" fill="none" stroke="#fff" stroke-width="1.1"/><path d="M3.2 6 L5.3 8 L10.5 2.2" fill="none" stroke="#fff" stroke-width="1.2"/></svg><span>Experience 5+ years in residential project management<br>with a strong portfolio of completed homes.</span></li>
    <li class="req__item" style="top:233px"><svg viewBox="0 0 12 12"><rect x="0.6" y="0.6" width="10.8" height="10.8" rx="3" fill="none" stroke="#fff" stroke-width="1.1"/><path d="M3.2 6 L5.3 8 L10.5 2.2" fill="none" stroke="#fff" stroke-width="1.2"/></svg><span>location : Bergen County, NJ</span></li>
    <li class="req__item" style="top:253px"><svg viewBox="0 0 12 12"><rect x="0.6" y="0.6" width="10.8" height="10.8" rx="3" fill="none" stroke="#fff" stroke-width="1.1"/><path d="M3.2 6 L5.3 8 L10.5 2.2" fill="none" stroke="#fff" stroke-width="1.2"/></svg><span>excellent leadership skills, leads teams with confidence and clarity</span></li>
    <li class="req__item req__item--wide" style="top:270px"><svg viewBox="0 0 12 12"><rect x="0.6" y="0.6" width="10.8" height="10.8" rx="3" fill="none" stroke="#fff" stroke-width="1.1"/><path d="M3.2 6 L5.3 8 L10.5 2.2" fill="none" stroke="#fff" stroke-width="1.2"/></svg><span>communicates seamlessly with architects , engineers, designers<br>and clients</span></li>
    <li class="req__item" style="top:312px"><svg viewBox="0 0 12 12"><rect x="0.6" y="0.6" width="10.8" height="10.8" rx="3" fill="none" stroke="#fff" stroke-width="1.1"/><path d="M3.2 6 L5.3 8 L10.5 2.2" fill="none" stroke="#fff" stroke-width="1.2"/></svg><span>knows how to manage budgets and timelines without<br>compromising quality</span></li>
    <li class="req__item" style="top:352px"><svg viewBox="0 0 12 12"><rect x="0.6" y="0.6" width="10.8" height="10.8" rx="3" fill="none" stroke="#fff" stroke-width="1.1"/><path d="M3.2 6 L5.3 8 L10.5 2.2" fill="none" stroke="#fff" stroke-width="1.2"/></svg><span>solves problems with a positive solution first mindset</span></li>
    <li class="req__item" style="top:371px"><svg viewBox="0 0 12 12"><rect x="0.6" y="0.6" width="10.8" height="10.8" rx="3" fill="none" stroke="#fff" stroke-width="1.1"/><path d="M3.2 6 L5.3 8 L10.5 2.2" fill="none" stroke="#fff" stroke-width="1.2"/></svg><span>pays attention to every detail because in luxury the small<br>things are the big things</span></li>
  </ul>

  <p class="site-url">www.ridgelanebuilders.com</p>
</section>

</body>
</html>
```